KVRo Business Cards

We need a business card design. We are a Technology (Audio Visual) design, sales and installation company. Looking for a double sided design, clean

Contact Information for Business Card

Clean, modern look, 2 sided

Font styles to use
Sans Serif

```html
<!DOCTYPE html>
<html lang="en">
<head>
<meta charset="UTF-8">
<title>KVRo Business Cards</title>
<link href="https://fonts.googleapis.com/css2?family=Montserrat:wght@400;500;600;800&display=swap" rel="stylesheet">
<style>
  :root {
    --navy: #1b303e;
    --orange: #f79622;
    --white: #ffffff;
    --page: #e4e4e4;
    --wordmark-dark: #2e5a6b;
  }
  html, body {
    margin: 0;
    padding: 0;
    width: 1125px;
    height: 1200px;
    overflow: hidden;
    background: var(--page);
    font-family: "Montserrat", Arial, sans-serif;
  }
  .card {
    position: absolute;
    overflow: hidden;
  }
  .card--front {
    left: 176px;
    top: 106px;
    width: 826px;
    height: 472px;
    background: var(--white);
  }
  .card--back {
    left: 167px;
    top: 634px;
    width: 844px;
    height: 482px;
    background: var(--navy);
  }
  .wordmark {
    position: absolute;
    left: 0;
    right: 0;
    text-align: center;
    font-weight: 800;
    letter-spacing: -2px;
    line-height: 1;
  }
  .card--front .wordmark {
    top: 76px;
    font-size: 176px;
    color: var(--navy);
  }
  .card--back .wordmark {
    top: 154px;
    font-size: 180px;
    color: var(--wordmark-dark);
  }
  .identity {
    position: absolute;
    left: 0;
    top: 317px;
    width: 434px;
    height: 155px;
    background: var(--navy);
    color: var(--white);
  }
  .identity__name {
    position: absolute;
    left: 45px;
    top: 17px;
    margin: 0;
    font-size: 25px;
    font-weight: 600;
    letter-spacing: 0.3px;
  }
  .identity__role {
    position: absolute;
    left: 45px;
    top: 52px;
    margin: 0;
    font-size: 17px;
    font-weight: 600;
  }
  .identity__address {
    position: absolute;
    left: 46px;
    top: 82px;
    margin: 0;
    font-size: 17px;
    font-weight: 400;
    font-style: normal;
    line-height: 23px;
  }
  .contact {
    position: absolute;
    left: 436px;
    top: 317px;
    right: 0;
    height: 155px;
    background: var(--orange);
    color: var(--white);
  }
  .contact__list {
    list-style: none;
    margin: 0;
    padding: 0;
    position: absolute;
    right: 44px;
    top: 24px;
  }
  .contact__item {
    display: flex;
    justify-content: flex-end;
    align-items: center;
    gap: 10px;
    height: 24px;
    font-size: 17px;
  }
  .contact__icon {
    width: 15px;
    height: 15px;
    fill: var(--white);
  }
</style>
</head>
<body>
  <section class="card card--front" aria-label="Business card front">
    <div class="wordmark">KVRo</div>

    <div class="identity">
      <h1 class="identity__name">DANIEL REYES</h1>
      <p class="identity__role">President</p>
      <address class="identity__address">4120 Juniper Court<br>Fairview, Oregon 97024</address>
    </div>

    <div class="contact">
      <ul class="contact__list">
        <li class="contact__item">555-304-7182
          <svg class="contact__icon" viewBox="0 0 16 16" aria-hidden="true"><path d="M3.5 1.5l2.5 3-1.5 1.8c.8 1.9 2.3 3.4 4.2 4.2l1.8-1.5 3 2.5-1.3 2.5C7 13.7 2.3 9 2 3z"/></svg>
        </li>
        <li class="contact__item">555-861-2049
          <svg class="contact__icon" viewBox="0 0 16 16" aria-hidden="true"><path d="M4 0h8a1 1 0 011 1v14a1 1 0 01-1 1H4a1 1 0 01-1-1V1a1 1 0 011-1zm.8 1.8v10.6h6.4V1.8zM8 13.2a.9.9 0 100 1.8.9.9 0 000-1.8z"/></svg>
        </li>
        <li class="contact__item">info@kvro.com
          <svg class="contact__icon" viewBox="0 0 16 16" aria-hidden="true"><path d="M1 3.5h14v9H1zm1.3 1.2L8 9l5.7-4.3z" fill-rule="evenodd"/></svg>
        </li>
        <li class="contact__item">www.kvro.com
          <svg class="contact__icon" viewBox="0 0 16 16" aria-hidden="true"><circle cx="8" cy="8" r="7"/><path d="M4 5l2-1 1 2-1 2-2 0zM9 9l3 0 0 3-2 1z" fill="var(--orange)"/></svg>
        </li>
      </ul>
    </div>
  </section>

  <section class="card card--back" aria-label="Business card back">
    <div class="wordmark">KVRo</div>
  </section>
</body>
</html>
```